We are in search of a new business card design for our business. We have a Mexican Grocery Store called Tortilla Grove Market, we would like to see that some have mexican design, but we are open to any type of designs.

Phone: to be announced
Fax: to be announced

Address is:
2415 Calloway Blvd
Larkfield, MD 21390

```html
<!DOCTYPE html>
<html lang="en">
<head>
<meta charset="utf-8">
<title>Tortilla Grove Market – Business Card</title>
<link rel="stylesheet" href="https://fonts.googleapis.com/css2?family=Open+Sans:wght@400;600;700&display=swap">
<style>
  :root {
    --backdrop: #e9e9e9;
    --card: #ffffff;
    --name-red: #a51c24;
    --ink: #2b2b2b;
    --muted: #4a4a4a;
    --band-green: #2aae4a;
    --band-orange: #f6a81f;
    --band-red: #dc2626;
  }
  html, body {
    margin: 0;
    padding: 0;
    width: 1200px;
    height: 977px;
    overflow: hidden;
    background: var(--backdrop);
    font-family: "Open Sans", Arial, sans-serif;
  }
  .business-card {
    position: absolute;
    left: 75px;
    top: 188px;
    width: 1050px;
    height: 600px;
    background: var(--card);
    box-shadow: 0 10px 30px rgba(0,0,0,0.18);
    overflow: hidden;
  }
  .contact {
    position: absolute;
    left: 125px;
    top: 245px;
  }
  .contact__name {
    margin: 0;
    font-size: 34px;
    font-weight: 600;
    color: var(--name-red);
    line-height: 1.1;
  }
  .contact__role {
    margin: 2px 0 0;
    font-size: 20px;
    font-weight: 700;
    color: var(--ink);
  }
  .contact__details {
    margin: 30px 0 0;
    font-size: 21px;
    line-height: 1.35;
    color: var(--muted);
    font-style: normal;
  }
  .brand {
    position: absolute;
    left: 620px;
    top: 160px;
    display: flex;
    align-items: center;
    gap: 16px;
  }
  .brand__dot {
    flex: 0 0 auto;
    width: 34px;
    height: 34px;
    border-radius: 50%;
    background: var(--band-red);
  }
  .brand__name {
    font-size: 32px;
    font-weight: 700;
    color: var(--name-red);
    line-height: 1.15;
    width: 260px;
  }
  .color-band {
    position: absolute;
    left: 0;
    bottom: 0;
    width: 100%;
    height: 46px;
    display: flex;
    gap: 8px;
  }
  .color-band__green { flex: 0 0 150px; background: var(--band-green); }
  .color-band__orange { flex: 1 1 auto; background: var(--band-orange); }
  .color-band__red { flex: 0 0 120px; background: var(--band-red); }
</style>
</head>
<body>
  <div class="business-card">
    <div class="brand">
      <span class="brand__dot"></span>
      <span class="brand__name">Tortilla Grove Market</span>
    </div>
    <div class="contact">
      <h1 class="contact__name">Mateo Carrión</h1>
      <p class="contact__role">Co-Founder</p>
      <address class="contact__details">
        2415 Calloway Blvd<br>
        Larkfield, MD 21390<br>
        Phone: 01 47 62 38 15
      </address>
    </div>
    <div class="color-band">
      <span class="color-band__green"></span>
      <span class="color-band__orange"></span>
      <span class="color-band__red"></span>
    </div>
  </div>
</body>
</html>
```